Courier Business needs a Business Card Design !!!

My new company needs a business card design. Our company name is Maple Dart Courier & Delivery Services. We will be servicing residential , government and business clients in the City of Yellowknife, Northwest Territories, Canada. I would like the following information included on the card: Name- Calvin Oxley. Title- Owner. Company- Maple Dart Courier & Delivery Services. Address- PO Box 5918 , Yellowknife , NWT, X0E 4K3. Phone- 867-555-0193. Email- mapledartdelivery@postfern.example. Facebook- www.socialpage.example/mapledartdelivery. I would like my double sided card to be the standard size of 84mm x 55mm. No borders. Use CMYK mode.1039x 697 pixels at least. I would like my logo to take up at least one quarter of the area of one side of the card. Text should be at least 8 point with perhaps my name being 10 point and my company name being 12-15 point . It should have clear readable font. Please use one or two bold colors. I am trying to attract the business community so a professional look might be best. My tag line is " On Time Every Time ". Nice safe margins please. We will be providing fast, reliable and professional delivery of envelopes and small packages within the City of Yellowknife. We offer 100% satisfaction or a complete refund. I have included a file of our logo. I like black, blue and red but am willing to look at what you feel would work best. I do not really like white as a background color.

Target Market(s)

Professionals , business owners. 30-50 years old

Industry/Entity Type

Residential

Contact Information for Business Card

As noted in brief

Font styles to use
Serif
Sans Serif

Colors
000000
0255a3
f04a50

Requirements
Must have
• My contact info. My logo
Nice to have
• Simple elegant design but still catches the eye
Should not have
• White background color

```html
<!DOCTYPE html>
<html lang="en">
<head>
<meta charset="utf-8">
<title>Maple Dart Courier &amp; Delivery Services – Business Card</title>
<link rel="stylesheet" href="https://fonts.googleapis.com/css2?family=Roboto:wght@300;400;700;900&display=swap">
<style>
  :root {
    --backdrop: #c9f5d9;
    --card-white: #ffffff;
    --card-blue: #1d4fe0;
    --card-blue-deep: #1238b8;
    --brand-red: #f04a50;
    --brand-blue: #0255a3;
    --accent-green: #a6d832;
    --text-white: #ffffff;
    --figure-tone: #c7d6e8;
    --figure-tone-back: #4d78ec;
  }
  * { box-sizing: border-box; margin: 0; padding: 0; }
  html, body { width: 1200px; height: 856px; overflow: hidden; }
  body {
    background: var(--backdrop);
    font-family: "Roboto", Arial, sans-serif;
    display: flex;
    align-items: center;
    justify-content: center;
    gap: 48px;
  }
  .card {
    width: 520px;
    height: 340px;
    border-radius: 34px;
    position: relative;
    overflow: hidden;
    box-shadow: 0 10px 28px rgba(40, 90, 60, 0.18);
  }

  /* Front side */
  .card--front { background: var(--card-white); }
  .front__mark {
    position: absolute;
    left: 300px;
    top: 78px;
    width: 110px;
    height: 62px;
    border-radius: 30px 30px 12px 12px;
    background: linear-gradient(120deg, #9fc3ef, var(--figure-tone));
  }
  .front__company {
    position: absolute;
    left: 0; right: 0;
    top: 132px;
    text-align: center;
    font-weight: 900;
    font-size: 19px;
    letter-spacing: 0.2px;
    color: var(--brand-red);
    text-transform: uppercase;
    line-height: 1.2;
  }
  .front__tagline {
    position: absolute;
    left: 0; right: 0;
    top: 186px;
    text-align: center;
    font-size: 10px;
    font-weight: 700;
    letter-spacing: 2px;
    color: var(--brand-blue);
    text-transform: uppercase;
  }
  .front__person {
    position: absolute;
    left: 0; right: 0;
    top: 226px;
    text-align: center;
    color: var(--brand-blue);
  }
  .person__name {
    font-size: 18px;
    text-transform: uppercase;
    display: inline-block;
    padding: 0 6px 2px;
    border-bottom: 1.5px solid var(--accent-green);
  }
  .person__first { font-weight: 900; }
  .person__last { font-weight: 300; }
  .person__title {
    font-size: 15px;
    font-weight: 300;
    margin-top: 1px;
  }

  /* Back side */
  .card--back {
    background: linear-gradient(160deg, var(--card-blue), var(--card-blue-deep));
  }
  .back__figure {
    position: absolute;
    left: 140px;
    top: 38px;
    width: 250px;
    height: 100px;
    border-radius: 50px 40px 20px 20px;
    background: linear-gradient(90deg, rgba(77,120,236,0) 0%, var(--figure-tone-back) 45%, #6f93f0 100%);
  }
  .back__contact {
    position: absolute;
    left: 268px;
    top: 166px;
    color: var(--text-white);
    font-size: 11.5px;
    line-height: 1.35;
    list-style: none;
  }
  .contact__address { margin-bottom: 2px; }
  .contact__row { display: flex; align-items: center; gap: 6px; }
  .contact__phone { font-weight: 700; font-size: 12.5px; }
  .contact__icon {
    width: 11px; height: 11px;
    flex: none;
    border-radius: 2px;
    background: var(--accent-green);
    display: flex; align-items: center; justify-content: center;
  }
  .contact__icon svg { width: 8px; height: 8px; }
</style>
</head>
<body>

  <section class="card card--front" aria-label="Business card front">
    <div class="front__mark" role="img" aria-label="Running bird mascot illustration"></div>
    <h1 class="front__company">Maple Dart<br>Courier &amp; Delivery Services</h1>
    <p class="front__tagline">On Time Every Time</p>
    <div class="front__person">
      <div class="person__name"><span class="person__first">Calvin</span><span class="person__last">Oxley</span></div>
      <div class="person__title">owner</div>
    </div>
  </section>

  <section class="card card--back" aria-label="Business card back">
    <div class="back__figure" role="img" aria-label="Running bird mascot illustration in white outline"></div>
    <ul class="back__contact">
      <li class="contact__address">PO Box 5918, Yellowknife,<br>NWT, X0E 4K3</li>
      <li class="contact__row contact__phone">
        <span class="contact__icon">
          <svg viewBox="0 0 10 10"><path d="M2 1 L4 1 L4.6 3 L3.5 3.8 Q4.3 5.6 6.2 6.5 L7 5.4 L9 6 L9 8 Q9 9 8 9 Q1 8.5 1 2 Q1 1 2 1 Z" fill="#1238b8"/></svg>
        </span>867-555-0193
      </li>
      <li class="contact__row">
        <span class="contact__icon">
          <svg viewBox="0 0 10 10"><rect x="1" y="2.5" width="8" height="5" fill="none" stroke="#1238b8" stroke-width="1"/><path d="M1 2.5 L5 5.5 L9 2.5" fill="none" stroke="#1238b8" stroke-width="1"/></svg>
        </span>mapledartdelivery@postfern.example
      </li>
      <li class="contact__row">
        <span class="contact__icon"></span>/mapledartdelivery
      </li>
    </ul>
  </section>

</body>
</html>
```